Business card design for a dynamic IT consulting company

We need a business card design for a young firm, specialized in the Telecommunications/Consulting industry. The name of the company is Brask and Partners Business Consulting Ltd. (Short name: Brask and Partnes)
Brask = solve read reverse, so we aim to be uncomplicated and solution-oriented. The small pipe in our logo is also related to the word solve. So we need a new business card design, which is simple, eye catching and something non traditional (I would probably prefer a square shaped design rather than a rectangle, but open for suggestions). Attached our logo.

Target Market(s)

Usually our customers are Tier1 Telecoms providers (Q-Linkra, Parnexo, etc) and their executives.

Industry/Entity Type

Business

Contact Information for Business Card

Name: Gergely Halmindo
Email: g.halmindo@braskpartnera.hu
Web: www.braskpartnera.hu
Mobile: +36 30 555 0192
Title: Managing Director

Optional:
Company name: Brask and Partners Ltd.
Address: 1047 Budapest, Ravaszi str. 17/B, Hungary

Font styles to use
Other font styles liked:
• helveticaneue_medium, Prime Regular are used now.

Colors

Designer to choose colors to be used in the design.

Requirements
Must have
• I would like to have a 2 sided design.
Nice to have
• I thought if we make the logo a bit bigger (without the company name), that could go to the back with the company name below. I though, if the pipe in the logo is somehow touchable on the business card, would be nice and unique.

```html
<!DOCTYPE html>
<html lang="en">
<head>
<meta charset="UTF-8">
<title>Brask and Partners – Business Card</title>
<link rel="stylesheet" href="https://fonts.googleapis.com/css2?family=Arimo:wght@400;700&display=swap">
<style>
  :root {
    --backdrop: #8a6444;
    --card-dark: #5d5f61;
    --card-light: #f7f7f6;
    --accent-blue: #1e9ad8;
    --accent-magenta: #b0268c;
    --text-white: #ffffff;
    --text-grey: #5a5c5e;
    --rule: rgba(255,255,255,0.45);
  }
  * { margin: 0; padding: 0; box-sizing: border-box; }
  html, body {
    width: 1200px; height: 960px; overflow: hidden;
    background: var(--backdrop);
    font-family: "Arimo", Helvetica, Arial, sans-serif;
  }
  .canvas { position: relative; width: 1200px; height: 960px; }
  .card {
    position: absolute;
    width: 343px; height: 342px;
    box-shadow: 2px 3px 5px rgba(0,0,0,0.35);
  }
  .card-front {
    left: 200px; top: 306px;
    background: var(--card-dark);
    color: var(--text-white);
    padding: 33px 34px 0 35px;
    text-transform: uppercase;
    font-size: 14px;
    line-height: 18px;
  }
  .holder-name {
    color: var(--accent-blue);
    font-weight: 700;
    font-size: 18px;
    line-height: 20px;
  }
  .holder-title { margin-top: 2px; font-size: 15px; }
  .divider {
    border: 0;
    border-top: 1px dashed var(--rule);
    width: 274px;
    margin-top: 30px;
  }
  .address { margin-top: 38px; }
  .divider-lower { margin-top: 38px; }
  .contact { margin-top: 36px; font-size: 13.5px; }
  .contact-label { color: var(--accent-blue); font-weight: 700; }

  .card-back {
    left: 651px; top: 305px;
    background: var(--card-light);
    color: var(--text-grey);
  }
  .brand {
    position: absolute; left: 0; right: 0; top: 188px;
    display: flex; align-items: center; justify-content: center; gap: 10px;
  }
  .brand-mark { width: 12px; height: 12px; background: var(--accent-blue); }
  .brand-name { font-size: 27px; font-weight: 400; color: var(--text-grey); }
  .website {
    position: absolute; left: 0; right: 0; top: 293px;
    text-align: center;
    font-size: 12px;
    letter-spacing: 0.5em;
    color: var(--text-grey);
  }
</style>
</head>
<body>
<main class="canvas">
  <section class="card card-front" aria-label="Card front">
    <p class="holder-name">Gergely Halmindo</p>
    <p class="holder-title">Managing Director</p>
    <hr class="divider">
    <address class="address" style="font-style:normal">
      Brask and Partners Ltd.<br>
      1047 Budapest<br>
      Ravaszi str. 17/B, Hungary
    </address>
    <hr class="divider divider-lower">
    <p class="contact">
      <span class="contact-label">Cell:</span> +36 30 555 0192<br>
      <span class="contact-label">Email:</span> g.halmindo@braskpartnera.hu
    </p>
  </section>

  <section class="card card-back" aria-label="Card back">
    <div class="brand">
      <span class="brand-mark"></span>
      <span class="brand-name">Brask &amp; Partners</span>
    </div>
    <p class="website">www.braskpartnera.hu</p>
  </section>
</main>
</body>
</html>
```